Graphic design on webpages considering optimisation

Hi,

I would like to make the pages of my website look better. The looks must tie with the landing page, which I will not change.

Ping me an email with any questions. I have been on Sketch Harbor for the brimvault.com page and am very pleased with its looks.

Industry/Entity Type

Graphic Design

```html
<!DOCTYPE html>
<html lang="fr">
<head>
<meta charset="utf-8">
<title>Brimvault – Valeurs ajoutées</title>
<link rel="stylesheet" href="https://fonts.googleapis.com/css2?family=Arimo:wght@400;700&family=Noto+Serif:ital,wght@1,700&display=swap">
<style>
:root{
  --navy:#4a5b8e;
  --navy-dark:#3b4a78;
  --ink:#3d4f86;
  --text:#555;
  --muted:#777;
  --orange:#f7941d;
  --orange-dark:#e07f0c;
  --panel:#f3f3f3;
  --line:#e1e1e1;
  --page:#fafafa;
  --footer-band:#e9e9e9;
  --footer:#0b0b0b;
  --nav-active:#a9bde3;
}
*{box-sizing:border-box;margin:0;padding:0}
html,body{width:768px;height:1200px;overflow:hidden;background:var(--page)}
body{font-family:"Arimo",Arial,sans-serif;color:var(--text)}
.frame{position:absolute;left:0;top:0;width:750px;height:1172px;transform:scale(1.024);transform-origin:0 0;background:var(--page)}
.abs{position:absolute}
.sheet{left:95px;top:0;width:590px;height:940px;background:#fff}
.brand{left:97px;top:18px;font-size:25px;font-weight:700;letter-spacing:1px;color:#666}
.brand-dot{display:inline-block;width:13px;height:13px;background:var(--orange);border-radius:50%;margin-right:6px;vertical-align:1px}
.phone{left:528px;top:17px;display:flex;align-items:center;gap:9px;font-size:13px;font-weight:700;color:var(--ink);font-family:"Noto Serif",serif;font-style:normal}
.phone span{font-family:"Arimo",sans-serif;letter-spacing:.5px}
.nav{left:95px;top:66px;width:590px;height:27px;display:flex;background:linear-gradient(#fff,#ececec);border-bottom:1px solid #ddd}
.nav a{flex:1;text-align:center;font-size:8.5px;line-height:27px;color:#333;text-decoration:none;border-right:1px solid #ddd}
.nav a:last-child{border-right:0}
.nav a.active{background:var(--nav-active);color:#223}
.bar{background:var(--navy);color:#fff;font-size:11px;height:27px;display:flex;align-items:center}
.bar.title{padding-left:9px;text-transform:uppercase;letter-spacing:.2px}
.side-bar .ico{width:29px;height:27px;display:flex;align-items:center;justify-content:center;border-right:1px solid #7f8db5;margin-right:7px}
.hero{left:101px;top:126px;width:407px;height:84px;background:linear-gradient(180deg,#8c6a4a 0%,#c09470 45%,#d8ccbf 70%,#a0744f 100%)}
.intro{left:101px;top:218px;width:407px;font-size:7.5px;line-height:10px;color:var(--muted)}
.intro p+p{margin-top:10px}
.h2{font-size:10.5px;color:var(--ink);text-transform:uppercase;letter-spacing:.2px}
.tabs{left:101px;top:331px;display:flex;gap:6px}
.tab{height:21px;padding:0 16px;font-size:9px;line-height:21px;color:#fff;background:var(--navy);border-radius:3px 3px 0 0}
.tab.current{background:var(--panel);color:var(--ink);width:82px;text-align:center}
.tab-panel{left:101px;top:351px;width:407px;height:160px;background:var(--panel);padding:11px 12px;font-size:7.5px;line-height:9.5px;color:var(--muted)}
.ticks{list-style:none;margin-top:10px}
.ticks li{color:#444;margin-bottom:5.5px;padding-left:11px;position:relative}
.ticks li::before,.bullets li::before{content:"››";position:absolute;left:0;color:var(--ink);font-weight:700}
.acc{left:101px;top:562px;width:407px}
.acc-row{height:27.5px;display:flex;align-items:center;color:#fff;font-size:10.5px;background:var(--navy);border-bottom:1px solid #fff}
.acc-row .chev{width:31px;height:100%;display:flex;align-items:center;justify-content:center;border-right:1px solid #8391b8;margin-right:6px}
.acc-body{background:var(--panel);height:147px;padding:6px 5px;font-size:7.5px;line-height:9.5px;color:#444}
.bullets{list-style:none;margin-top:14px;padding-left:5px}
.bullets li{position:relative;padding-left:11px;color:var(--muted);margin-bottom:9px}
.links{left:515px;top:125px;width:168px;list-style:none}
.links li{height:29px;display:flex;align-items:center;font-size:8.5px;color:#888;border-bottom:1px dashed #ddd}
.links li b{color:var(--ink);width:35px;text-align:center;font-size:11px}
.cta{background:linear-gradient(#fba63a,var(--orange-dark));color:#fff;font-family:"Noto Serif",serif;font-style:italic;font-weight:700;font-size:13px;text-align:center;border-radius:3px}
.partner{left:525px;top:405px;display:flex;align-items:center;gap:6px}
.benefit{left:515px;top:474px;width:168px;height:123px;background:#eee;text-align:center}
.client-card{margin:8px auto 0;width:136px;height:46px;background:#fff;border-radius:3px;display:flex;align-items:center;justify-content:center;font-size:15px;color:#555}
.benefit p{margin-top:4px;font-size:7.5px;line-height:10px;color:var(--ink)}
.pager{display:flex;justify-content:center;margin-top:6px}
.pager span{width:21px;height:21px;border-radius:50%;background:var(--orange);color:#fff;font-size:11px;font-weight:700;line-height:21px;margin:0 -1px}
.band{left:0;top:940px;width:750px;height:190px;background:var(--footer-band);box-shadow:inset 0 6px 8px -6px rgba(0,0,0,.35)}
.band h3{position:absolute;left:0;width:750px;top:24px;text-align:center;font-weight:400;font-size:13px;color:var(--ink)}
.cloud{width:165px;height:106px;border-radius:52px 60px 14px 14px;background:radial-gradient(circle at 50% 45%,#fff 40%,#e3e3e3 100%);box-shadow:0 2px 4px rgba(0,0,0,.2)}
.cloud-label{height:27px;width:147px;display:flex;align-items:center;gap:8px;padding-left:8px}
.play{width:22px;height:22px;border:2px solid #fff;border-radius:50%;display:flex;align-items:center;justify-content:center}
.footer{left:0;top:1130px;width:750px;height:42px;background:var(--footer)}
.footer small{position:absolute;left:103px;top:19px;font-size:7.5px;color:#999}
.social{position:absolute;top:11px;width:21px;height:21px;border-radius:3px}
</style>
</head>
<body>
<div class="frame">
  <div class="abs sheet"></div>

  <header>
    <div class="abs brand"><span class="brand-dot"></span>BRIMVAULT</div>
    <div class="abs phone">
      <svg width="15" height="15" viewBox="0 0 15 15"><rect width="15" height="15" rx="2" fill="#3f7fcf"/><path d="M4 3.5c1 0 1.5 1.8 1 2.3l-.6.6c.6 1.4 1.6 2.4 3 3l.6-.6c.5-.5 2.3 0 2.3 1 0 1-1 1.8-2 1.7C5.5 11 3.9 9.4 3.4 6c-.1-1.2.6-2.5.6-2.5z" fill="#fff"/></svg>
      <span>+33(0)145 208 316</span>
    </div>
    <nav class="abs nav">
      <a>Accueil</a><a>Produits</a><a class="active">Valeurs Ajoutées</a><a>Clients</a><a>Service</a><a>Société</a><a>Contact</a>
    </nav>
  </header>

  <main>
    <div class="abs bar title" style="left:101px;top:98px;width:407px">Services &amp; Support</div>
    <div class="abs hero" role="img" aria-label="Photo d'un ordinateur portable, de lunettes et d'une souris sur un bureau en bois"></div>
    <div class="abs intro">
      <p>Notre activité d'intégrateur autour des solutions LedgerSky ne date pas d'hier, mais de 2009, après que le fondateur de Brimvault, Claire Morand, ait quitté de son poste de consultant chez LedgerSky Angleterre pour lancer sa propre activité en France.</p>
      <p>Une telle proximité avec l'éditeur et cette longévité ont laissé le temps à Brimvault d'élaborer et de consolider son offre, unique sur le marché francophone, de services complémentaires à LedgerSky.</p>
    </div>
    <h2 class="abs h2" style="left:101px;top:305px">Services Brimvault complémentaires à LedgerSky</h2>

    <div class="abs tabs">
      <div class="tab current">Consulting</div>
      <div class="tab">Support Technique</div>
      <div class="tab">Formation</div>
    </div>
    <div class="abs tab-panel">
      <p>Nos consultants senior ont plus de 12 ans d'expérience dans la finance-comptabilité, le CRM et le décisionnel, expérience tirée de conduites de projets dans des sociétés de tailles, de secteurs d'activité et de pays divers et variés. Leur implication dans ces succès leur donne une légitimité pour vous accompagner lors des étapes clé de votre projet, en particulier dans les domaines suivants :</p>
      <ul class="ticks">
        <li>Appréhension de vos objectifs</li>
        <li>Compréhension de vos besoins et proposition de solutions LedgerSky</li>
        <li>Spécification et développement de modules complémentaires à LedgerSky</li>
        <li>Proposition de bonnes pratiques</li>
        <li>Conduite des projets d'implémentation des solutions LedgerSky</li>
        <li>Mesure des retours sur investissements</li>
      </ul>
    </div>

    <h2 class="abs h2" style="left:103px;top:541px">Les bénéfices communs à tous les produits LedgerSky :</h2>
    <div class="abs acc">
      <div class="acc-row"><span class="chev"><svg width="13" height="10" viewBox="0 0 13 10" fill="none" stroke="#fff" stroke-width="2"><path d="M1 5l5.5-4 5.5 4M1 9.5l5.5-4 5.5 4"/></svg></span>Les logiciels LedgerSky..</div>
      <div class="acc-body">
        <p>Les logiciels LedgerSky sont accessibles via internet en ce qu'on appelle le mode SaaS ou autrement dit dans le Cloud. A moins que vous n'en soyez pas équipés (ce qui devient extrêmement rare) ou que votre Fournisseur d'Accès Internet ne parvient pas à vous fournir un débit raisonnable, vous pourrez profiter de</p>
        <ul class="bullets">
          <li>Grâce à l'accélération du délai de fourniture au Client de sa commande, obtenue par une meilleure gestion des stocks multi-sites et un réapprovisionnement adapté, une fluidité du processus partant de la commande à la facturation et à la livraison.</li>
          <li>Grâce aux propositions personnalisées aux profils des Clients, comme des réductions de prix volume accordées à des Clients le méritant ou des promotions sur des articles restant trop longtemps en stocks et correspondant aux souhaits potentiels de certains Clients.</li>
        </ul>
      </div>
      <div style="height:2px"></div>
      <div class="acc-row"><span class="chev"><svg width="13" height="10" viewBox="0 0 13 10" fill="none" stroke="#fff" stroke-width="2"><path d="M1 1l5.5 4 5.5-4M1 5.5l5.5 4 5.5-4"/></svg></span>Un tarif hyper concurrentiel..</div>
      <div class="acc-row"><span class="chev"><svg width="13" height="10" viewBox="0 0 13 10" fill="none" stroke="#fff" stroke-width="2"><path d="M1 1l5.5 4 5.5-4M1 5.5l5.5 4 5.5-4"/></svg></span>Une réactivité hors..</div>
      <div class="acc-row"><span class="chev"><svg width="13" height="10" viewBox="0 0 13 10" fill="none" stroke="#fff" stroke-width="2"><path d="M1 1l5.5 4 5.5-4M1 5.5l5.5 4 5.5-4"/></svg></span>Des économies conséquentes..</div>
      <div class="acc-row"><span class="chev"><svg width="13" height="10" viewBox="0 0 13 10" fill="none" stroke="#fff" stroke-width="2"><path d="M1 1l5.5 4 5.5-4M1 5.5l5.5 4 5.5-4"/></svg></span>Une rapidité..</div>
      <div class="acc-row"><span class="chev"><svg width="13" height="10" viewBox="0 0 13 10" fill="none" stroke="#fff" stroke-width="2"><path d="M1 1l5.5 4 5.5-4M1 5.5l5.5 4 5.5-4"/></svg></span>Une productivité ..</div>
      <div class="acc-row"><span class="chev"><svg width="13" height="10" viewBox="0 0 13 10" fill="none" stroke="#fff" stroke-width="2"><path d="M1 1l5.5 4 5.5-4M1 5.5l5.5 4 5.5-4"/></svg></span>Une tranquillité d'esprit..</div>
      <div class="acc-row"><span class="chev"><svg width="13" height="10" viewBox="0 0 13 10" fill="none" stroke="#fff" stroke-width="2"><path d="M1 1l5.5 4 5.5-4M1 5.5l5.5 4 5.5-4"/></svg></span>Un chiffre d'affaires..</div>
    </div>
  </main>

  <aside>
    <div class="abs bar side-bar" style="left:515px;top:98px;width:168px"><span class="ico"><svg width="14" height="11" viewBox="0 0 14 11" fill="#fff"><rect width="3" height="3"/><rect x="4" width="10" height="3"/><rect y="4" width="3" height="3"/><rect x="4" y="4" width="10" height="3"/><rect y="8" width="3" height="3"/><rect x="4" y="8" width="10" height="3"/></svg></span>IMPORTANT LINKS</div>
    <ul class="abs links">
      <li><b>››</b>Nos Services</li><li><b>››</b>Conseil</li><li><b>››</b>Support</li><li><b>››</b>Developpement</li><li><b>››</b>Formation</li><li style="border:0"><b>››</b>Decouverte</li>
    </ul>
    <div class="abs bar side-bar" style="left:515px;top:299px;width:168px"><span class="ico" style="font-family:'Noto Serif',serif;font-style:italic;font-weight:700;font-size:15px">i</span>UNE INFO ?</div>
    <div class="abs cta" style="left:525px;top:334px;width:146px;height:26px;line-height:26px">Contactez nous</div>
    <div class="abs bar side-bar" style="left:515px;top:372px;width:168px"><span class="ico"><svg width="13" height="13" viewBox="0 0 13 13" fill="#fff"><rect x="1" y="3" width="9" height="9"/><circle cx="5.5" cy="2.5" r="2"/><circle cx="10.5" cy="7.5" r="2"/></svg></span>NOS PARTENARIATS</div>
    <div class="abs partner">
      <span style="width:24px;height:24px;background:#2f4a6e;display:block"></span>
      <span style="width:60px;height:14px;background:#dfe3ea;display:block"></span>
    </div>
    <div class="abs bar side-bar" style="left:515px;top:448px;width:168px"><span class="ico"><svg width="13" height="13" viewBox="0 0 13 13" fill="#fff"><path d="M3 1h7v4a3.5 3.5 0 0 1-7 0z"/><rect x="5.5" y="8" width="2" height="2.5"/><rect x="3.5" y="10.5" width="6" height="1.5"/></svg></span>BÉNÉFICES CLIENT</div>
    <div class="abs benefit">
      <div class="client-card">Petalry.com</div>
      <p>30 K$ d'économies,<br>20% de réduction des CDF,<br>Situation stock immédiate,<br>10 h/mois économisées,<br>Livraison le jour même.</p>
      <div class="pager"><span>‹‹</span><span>››</span></div>
    </div>
    <div class="abs bar side-bar" style="left:515px;top:627px;width:168px"><span class="ico"><svg width="13" height="13" viewBox="0 0 13 13"><path d="M2 1l9 11" stroke="#fff" stroke-width="2"/></svg></span>DOCUMENTATION</div>
    <div class="abs cloud" role="img" aria-label="Illustration d'un nuage avec une loupe" style="left:528px;top:663px;width:144px;height:80px"></div>
    <div class="abs cta" style="left:527px;top:733px;width:145px;height:27px;line-height:27px;font-size:13.5px">Héberger ou pas?</div>
  </aside>

  <section class="abs band">
    <h3>AVANTAGES LEDGERSKY</h3>
    <div class="abs cloud" role="img" aria-label="Illustration d'un nuage avec un engrenage et un tournevis" style="left:99px;top:50px"></div>
    <div class="abs cta cloud-label" style="left:106px;top:146px"><span class="play"><svg width="8" height="9" viewBox="0 0 8 9"><path d="M0 0l8 4.5L0 9z" fill="#fff"/></svg></span>Manufacturing</div>
    <div class="abs cloud" role="img" aria-label="Illustration d'un nuage avec un camion de livraison" style="left:307px;top:50px"></div>
    <div class="abs cta cloud-label" style="left:314px;top:146px"><span class="play"><svg width="8" height="9" viewBox="0 0 8 9"><path d="M0 0l8 4.5L0 9z" fill="#fff"/></svg></span>Distribution</div>
    <div class="abs cloud" role="img" aria-label="Illustration d'un nuage avec une poignée de main" style="left:516px;top:50px"></div>
    <div class="abs cta cloud-label" style="left:523px;top:146px"><span class="play"><svg width="8" height="9" viewBox="0 0 8 9"><path d="M0 0l8 4.5L0 9z" fill="#fff"/></svg></span>Services</div>
  </section>

  <footer class="abs footer">
    <small>Copyright 2013 BRIMVAULT. All rights reserved.</small>
    <span class="social" style="left:606px;background:#3d5a98"></span>
    <span class="social" style="left:631px;background:#3fa9e0"></span>
    <span class="social" style="left:656px;background:#1f75b3"></span>
  </footer>
</div>
</body>
</html>
```